Business Card Design Project

Build kick ass business card.
Updates

I just uploaded the Veruxo Logo in AI format, for those that were asking. It's looking real good and we'll be reviewing the designs soon. Thanks. 

Target Market(s)

Businesses in many verticals. Focusing on information security.

Veruxo, LLC
Darren Colby
Principal Security Consultant
Mobile: +1-480-555-0137
Email: Darren.Colby@Veruxo.example
Web: www.veruxo.example

Industry/Entity Type

Business

Requirements
Must have
• Design must look high-end, hi-tech stylish and minimalist

Be different – one that stands out from thousands of others

Does not have to be traditional rectangle

Would like logo integrated

```html
<!DOCTYPE html>
<html lang="en">
<head>
<meta charset="utf-8">
<title>Veruxo Business Card Concepts</title>
<link rel="stylesheet" href="https://fonts.googleapis.com/css2?family=Source+Sans+3:wght@400;600;700&display=swap">
<style>
  :root {
    --bg-top: #8a3c8e;
    --bg-bottom: #c958ca;
    --blue-light: #25acdf;
    --blue-mid: #03a7e0;
    --blue-deep: #0062ad;
    --white: #ffffff;
    --ink: #3b3b3b;
    --ink-soft: #5a5a5a;
    --accent: #1f9bd6;
  }
  * { margin: 0; padding: 0; box-sizing: border-box; }
  html, body {
    width: 1200px; height: 800px; overflow: hidden;
  }
  body {
    background: linear-gradient(180deg, var(--bg-top) 0%, var(--bg-bottom) 100%);
    font-family: "Source Sans 3", sans-serif;
    position: relative;
  }
  .card {
    position: absolute;
    width: 559px; height: 310px;
    border-radius: 116px 0 0 0;
    overflow: hidden;
    background: var(--white);
  }
  .card--front-a { left: 26px; top: 43px; }
  .card--back-a  { left: 609px; top: 43px; }
  .card--back-b  { left: 26px; top: 395px; }
  .card--front-b { left: 609px; top: 395px; }

  .blue-field {
    position: absolute; left: 0; right: 0; bottom: 0;
    background: linear-gradient(180deg, var(--blue-light) 0%, var(--blue-mid) 40%, var(--blue-deep) 100%);
  }
  .card--front-a .blue-field { top: 0; }
  .card--front-b .blue-field { top: 124px; }

  .holder-name {
    position: absolute; left: 0; right: 0;
    text-align: center; color: var(--white);
    font-size: 24px; font-weight: 700; line-height: 28px;
  }
  .holder-title {
    position: absolute; left: 0; right: 0;
    text-align: center; color: var(--white);
    font-size: 16px; font-weight: 400; line-height: 20px;
  }
  .card--front-a .holder-name  { top: 119px; }
  .card--front-a .holder-title { top: 148px; }
  .card--front-b .holder-name  { top: 148px; }
  .card--front-b .holder-title { top: 176px; }

  .contact {
    position: absolute; top: 254px;
    color: var(--white); font-size: 12px; line-height: 16px;
    white-space: nowrap;
  }
  .contact .label { margin-right: 4px; }
  .contact--phone { left: 46px; }
  .contact--email { left: 200px; }
  .contact--web   { left: 398px; }

  .brand {
    position: absolute;
  }
  .brand-dot {
    position: absolute; left: -56px; top: 2px;
    width: 44px; height: 44px; border-radius: 50%;
    background: var(--accent);
  }
  .brand-name {
    display: block;
    font-size: 30px; font-weight: 400; line-height: 30px;
    letter-spacing: 1px; text-transform: uppercase;
    color: var(--ink);
  }
  .brand-tagline {
    display: block;
    font-size: 9px; line-height: 12px; letter-spacing: 1.4px;
    color: var(--ink-soft);
    margin-top: 1px;
  }
  .card--back-a .brand,
  .card--back-b .brand { left: 392px; top: 216px; }
  .card--front-b .brand { left: 254px; top: 61px; }
</style>
</head>
<body>

  <section class="card card--front-a">
    <div class="blue-field"></div>
    <p class="holder-name">Darren Colby</p>
    <p class="holder-title">Principal Security Consultant</p>
    <p class="contact contact--phone"><span class="label">m.</span>+1-480-555-0137</p>
    <p class="contact contact--email"><span class="label">e.</span>Darren.Colby@Veruxo.example</p>
    <p class="contact contact--web"><span class="label">w.</span>www.veruxo.example</p>
  </section>

  <section class="card card--back-a">
    <div class="brand">
      <span class="brand-dot"></span>
      <span class="brand-name">Veruxo</span>
      <span class="brand-tagline">network security solutions</span>
    </div>
  </section>

  <section class="card card--back-b">
    <div class="brand">
      <span class="brand-dot"></span>
      <span class="brand-name">Veruxo</span>
      <span class="brand-tagline">network security solutions</span>
    </div>
  </section>

  <section class="card card--front-b">
    <div class="brand">
      <span class="brand-dot"></span>
      <span class="brand-name">Veruxo</span>
      <span class="brand-tagline">network security solutions</span>
    </div>
    <div class="blue-field"></div>
    <p class="holder-name">Darren Colby</p>
    <p class="holder-title">Principal Security Consultant</p>
    <p class="contact contact--phone"><span class="label">m.</span>+1-480-555-0137</p>
    <p class="contact contact--email"><span class="label">e.</span>Darren.Colby@Veruxo.example</p>
    <p class="contact contact--web"><span class="label">w.</span>www.veruxo.example</p>
  </section>

</body>
</html>
```